Need a business card portraying store logo and up and coming business of quilt fabrics, apparel fabrics, notions and buttons. Our business name is Cherished Thread and Such. Am attaching logo. The design should communicate a growing business and warm atmosphere. Would like address and store hours and contact info displayed on card. Mon - Fri 9:30 to 5:00, Saturday 9:30 to 1:00. Address 238 W Elm Ave, Newton, KS 67392 email: cherishedthreadandsuch@mailbarn.net. Phone and fax 316-555-2847. After hours contact # 620-555-3916 Also like vintage sewing machines and dress forms if it works to incorporate fine, if not thats ok too.

```html
<!DOCTYPE html>
<html lang="en">
<head>
<meta charset="utf-8">
<title>Cherished Thread and Such — Business Card</title>
<link rel="stylesheet" href="https://fonts.googleapis.com/css2?family=Open+Sans:wght@400&family=Poiret+One&display=swap">
<style>
  :root {
    --page: #ffffff;
    --card-red: #af1a20;
    --band-red: #951c21;
    --label-red: #6f1216;
    --info-pink: #f0c4c6;
    --white: #ffffff;
    --pattern-light: #ad1a20;
    --pattern-dark: #9b171c;
  }
  * { margin: 0; padding: 0; box-sizing: border-box; }
  html, body {
    width: 1200px; height: 900px; overflow: hidden;
    background: var(--page);
  }
  .canvas { position: relative; width: 1200px; height: 900px; }

  .card { position: absolute; background: var(--card-red); overflow: hidden; }
  .card--front { left: 18px; top: 22px; width: 660px; height: 405px; }
  .card--back { left: 516px; top: 469px; width: 661px; height: 405px; }

  .front-band {
    position: absolute; left: 0; top: 33px; width: 100%; height: 130px;
    background: var(--band-red);
  }
  .brand {
    position: absolute; left: 130px; top: 50px;
    display: flex; align-items: center; gap: 18px;
  }
  .brand__button {
    width: 66px; height: 66px; border-radius: 50%; background: var(--white);
    flex: none;
  }
  .brand__name {
    font-family: "Open Sans", sans-serif; font-weight: 400;
    font-size: 27px; color: var(--white); letter-spacing: 0.5px;
  }

  .info { position: absolute; text-align: center; }
  .info__label {
    font-family: "Poiret One", sans-serif; font-size: 30px; font-weight: 400;
    color: var(--label-red); line-height: 30px;
  }
  .info__value {
    font-family: "Open Sans", sans-serif; font-size: 15px;
    color: var(--info-pink); line-height: 22px;
  }
  .info--left { left: 40px; width: 284px; }
  .info--right { left: 310px; width: 322px; }

  .pattern {
    position: absolute; inset: 0;
    background:
      radial-gradient(circle at 15% 20%, var(--pattern-dark) 0, transparent 45%),
      radial-gradient(circle at 60% 35%, var(--pattern-dark) 0, transparent 40%),
      radial-gradient(circle at 30% 85%, var(--pattern-dark) 0, transparent 45%),
      radial-gradient(circle at 85% 90%, var(--pattern-dark) 0, transparent 40%),
      var(--pattern-light);
  }
  .back-band {
    position: absolute; left: 231px; top: 220px; width: 430px; height: 78px;
    background: var(--band-red);
    display: flex; align-items: center; justify-content: center;
  }
  .back-band__name {
    font-family: "Open Sans", sans-serif; font-weight: 400;
    font-size: 20px; color: var(--white);
  }
</style>
</head>
<body>
<main class="canvas">
  <section class="card card--front" aria-label="Business card front">
    <div class="front-band"></div>
    <div class="brand">
      <span class="brand__button"></span>
      <span class="brand__name">Cherished Thread and Such</span>
    </div>

    <div class="info info--left" style="top:188px">
      <p class="info__label">phone/fax</p>
      <p class="info__value">316-555-2847</p>
    </div>
    <div class="info info--left" style="top:255px">
      <p class="info__label">address</p>
      <p class="info__value">238 W Elm Ave, Newton, KS 67392</p>
    </div>
    <div class="info info--left" style="top:318px">
      <p class="info__label">after hours</p>
      <p class="info__value"># 620-555-3916</p>
    </div>

    <div class="info info--right" style="top:199px">
      <p class="info__label">open</p>
      <p class="info__value">Mon- Fri 9:30 to 5:00</p>
      <p class="info__value">Saturday 9:30 to 1:00</p>
    </div>
    <div class="info info--right" style="top:299px">
      <p class="info__label">mail</p>
      <p class="info__value">cherishedthreadandsuch@mailbarn.net</p>
    </div>
  </section>

  <section class="card card--back" aria-label="Business card back">
    <div class="pattern" role="img" aria-label="Repeating pattern of vintage sewing machines and fabric rolls drawn in dark red outline"></div>
    <div class="back-band">
      <span class="back-band__name">Cherished Thread and Such</span>
    </div>
  </section>
</main>
</body>
</html>
```